Business card design for new, innovative company - BluePlinth

We are a new company looking for a business card design that is fun, different and quirky. Must use corporate colour green - CMYK C:55, M:0, Y:100, K:0, and corporate colour grey - C:0, M:0, Y: 0, K:70.

We have developed the first real time data application, in which people are able to profile the data of their existing customers in order to pull out more good fit clients to direct their marketing activities at.

Industry/Entity Type

Marketing

Requirements
Must have
• Logo, name, title, telephone number, fax number, email, website, address

```html
<!DOCTYPE html>
<html lang="en">
<head>
<meta charset="utf-8">
<title>BluePlinth business card</title>
<link rel="stylesheet" href="https://fonts.googleapis.com/css2?family=Arimo:wght@700&family=Didact+Gothic&display=swap">
<style>
  :root {
    --brand-green: #8dc63f;
    --brand-green-light: #d3f07e;
    --brand-green-deep: #9fd43a;
    --brand-grey: #6d6e71;
    --ink-grey: #5f6062;
    --card-white: #fdfdfd;
    --page: #ffffff;
    --print-dark: #1e1e1e;
  }
  * { margin: 0; padding: 0; box-sizing: border-box; }
  html, body { width: 980px; height: 1200px; overflow: hidden; background: var(--page); }
  .canvas { position: relative; width: 980px; height: 1200px; }

  .card {
    position: absolute;
    width: 795px;
    height: 481px;
    box-shadow: 0 10px 26px rgba(0,0,0,0.22);
  }
  .card-front {
    left: 92px; top: 53px;
    background: linear-gradient(180deg, var(--brand-green-light) 0%, var(--brand-green-deep) 100%);
    border: 2px solid #ffffff;
  }
  .card-back { left: 96px; top: 630px; background: var(--card-white); }

  .fingerprint {
    position: absolute;
    left: 661px; top: 23px;
    width: 102px; height: 133px;
    border-radius: 50%;
    background: radial-gradient(ellipse at center, #3a3a3a 0%, var(--print-dark) 70%, rgba(30,30,30,0.85) 100%);
  }
  .wordmark {
    position: absolute;
    left: 0; right: 0; top: 178px;
    text-align: center;
    font-family: "Arimo", Arial, sans-serif;
    font-weight: 700;
    font-size: 104px;
    line-height: 1;
    letter-spacing: -2px;
    color: var(--brand-grey);
  }
  .front-url {
    position: absolute;
    left: 395px; top: 327px;
    font-family: "Arimo", Arial, sans-serif;
    font-weight: 700;
    font-size: 25px;
    color: var(--brand-grey);
  }

  .back-brand {
    position: absolute;
    left: 58px; top: 215px;
    display: flex; align-items: center; gap: 10px;
    font-family: "Arimo", Arial, sans-serif;
    font-weight: 700;
    font-size: 28px;
    color: var(--brand-grey);
  }
  .back-brand .mark { width: 22px; height: 22px; background: var(--brand-green); }

  .divider {
    position: absolute;
    left: 243px; top: 116px;
    width: 4px; height: 268px;
    background: var(--brand-green);
  }
  .contact {
    position: absolute;
    left: 265px; top: 114px;
    font-family: "Didact Gothic", "Century Gothic", sans-serif;
    color: var(--ink-grey);
  }
  .contact-name {
    font-family: "Arimo", Arial, sans-serif;
    font-weight: 700;
    font-size: 22px;
    color: var(--brand-grey);
    margin-bottom: 26px;
  }
  .contact-list { list-style: none; }
  .contact-list li {
    display: flex; align-items: flex-start; gap: 12px;
    font-size: 23px; line-height: 28px;
    height: 35px;
  }
  .contact-list li.address { margin-top: 24px; height: auto; }
  .contact-list svg { flex: none; width: 22px; height: 22px; margin-top: 3px; fill: none; stroke: var(--brand-green); stroke-width: 2; }
  .contact-list svg .solid { fill: var(--brand-green); stroke: none; }
</style>
</head>
<body>
<main class="canvas">

  <section class="card card-front" aria-label="Card front">
    <div class="fingerprint" role="img" aria-label="Black fingerprint impression"></div>
    <div class="wordmark">BluePlinth</div>
    <div class="front-url">www.blueplinth.com</div>
  </section>

  <section class="card card-back" aria-label="Card back">
    <div class="back-brand"><span class="mark"></span>BluePlinth</div>
    <div class="divider"></div>
    <div class="contact">
      <p class="contact-name">Jenna Coleridge</p>
      <ul class="contact-list">
        <li>
          <svg viewBox="0 0 22 22" aria-hidden="true"><rect x="5" y="2" width="12" height="18" rx="2"/><line x1="9" y1="17" x2="13" y2="17"/></svg>
          <span>07700900461</span>
        </li>
        <li>
          <svg viewBox="0 0 22 22" aria-hidden="true"><path class="solid" d="M5 2 L9 2 L10 7 L7.5 9 C9 12.5 10.5 14 13 15.5 L15 13 L20 14 L20 18 C20 19.5 18.5 20.5 17 20 C9.5 18 4 12.5 2.5 5 C2.2 3.5 3.5 2 5 2 Z"/></svg>
          <span>01632 960735</span>
        </li>
        <li>
          <svg viewBox="0 0 22 22" aria-hidden="true"><rect x="2" y="5" width="18" height="12"/><polyline points="2,5 11,12 20,5"/></svg>
          <span>jenna.coleridge@northfieldsupply.com</span>
        </li>
        <li>
          <svg viewBox="0 0 22 22" aria-hidden="true"><circle cx="11" cy="11" r="9"/><ellipse cx="11" cy="11" rx="4" ry="9"/><line x1="2" y1="11" x2="20" y2="11"/><line x1="4" y1="6" x2="18" y2="6"/><line x1="4" y1="16" x2="18" y2="16"/></svg>
          <span>www.blueplinth.com</span>
        </li>
        <li class="address">
          <svg viewBox="0 0 22 22" aria-hidden="true"><path class="solid" d="M11 3 L21 10 L1 10 Z"/><rect class="solid" x="3" y="11" width="16" height="9"/><rect x="9" y="14" width="4" height="6" fill="#fff" stroke="none"/></svg>
          <span>27c Larkfield Road, Ely,<br>Cambridgeshire, CB7 4QN</span>
        </li>
      </ul>
    </div>
  </section>

</main>
</body>
</html>
```